Natural Medicine & Health/Fitness Coaching studio requires web page

Require a innovative web page for a studio that coaches clients to better health, nutrition and fitness. The studio compromises of Clinical Nutritionists, Naturopaths, Rehab Trainers, Personal Trainers and Sport Coaches. Would like to see earthy but bold designs emphasizing nutritional health and athletic performance.
Updates

Design only launched today.

Target Market(s)

All genders from 20's to 60's, as well as families

Industry/Entity Type

Nutritionist

Coding

Coded - Design and coding required

Number of Pages Required

3 page

Colors
abd037
3277b5
fbee3d
fece3e
33b8a4
f04a50

Requirements
Must have
• Online booking system, ability to message
• Home page
• Coaching/Fitness page
• Nutritional Medicine page
• Must be suitable for both Fitness and Nutrition

```html
<!DOCTYPE html>
<html lang="en">
<head>
<meta charset="utf-8">
<title>Verdant Fit – Nutritional Therapy</title>
<link rel="stylesheet" href="https://fonts.googleapis.com/css2?family=Roboto:wght@300;400;500;700;900&family=Roboto+Condensed:wght@400;700&display=swap">
<style>
:root{
  --green:#abd037;
  --green-dark:#8db522;
  --blue:#3277b5;
  --blue-dark:#245c8f;
  --yellow:#fbee3d;
  --gold:#fece3e;
  --teal:#33b8a4;
  --red:#f04a50;
  --ink:#333;
  --muted:#777;
  --light:#f1f2f4;
  --dark:#2b2b2b;
}
*{margin:0;padding:0;box-sizing:border-box}
html,body{width:1200px;height:2368px;overflow:hidden}
body{position:relative;background:#fff;font-family:"Roboto",Arial,sans-serif;color:var(--ink)}
.abs{position:absolute}
.btn{position:absolute;display:inline-block;background:var(--red);color:#fff;font:700 13px "Roboto",sans-serif;letter-spacing:.5px;padding:11px 18px;text-transform:uppercase}
.ph{position:absolute}

/* header */
.site-header{top:0;left:0;width:1200px;height:68px;background:#fff}
.brand{left:160px;top:10px;font:700 34px "Roboto Condensed",sans-serif;color:var(--green-dark);display:flex;align-items:center;gap:10px}
.brand .dot{width:14px;height:14px;border-radius:50%;background:var(--blue)}
.brand small{display:block;font:400 11px "Roboto",sans-serif;color:var(--blue);letter-spacing:1px;margin-top:-4px}
.booking{right:150px;top:17px;padding:9px 16px;font-size:12px;border-radius:2px}
.main-nav{top:68px;left:0;width:1200px;height:32px;background:var(--blue);display:flex;padding-left:150px}
.main-nav a{color:#fff;text-decoration:none;font:500 12px "Roboto",sans-serif;padding:0 16px;line-height:32px;text-transform:uppercase}
.main-nav a.active{background:var(--blue-dark)}

/* hero */
.hero{top:100px;left:0;width:1200px;height:320px;background:linear-gradient(90deg,#f4f5f6,#e6e8ea)}
.hero .intro{left:160px;top:70px;font:300 30px "Roboto",sans-serif;color:var(--blue)}
.hero h1{position:absolute;left:160px;top:104px;font:900 64px "Roboto Condensed",sans-serif;color:var(--green-dark);line-height:1}
.hero p{left:160px;top:180px;width:330px;font-size:12px;line-height:17px;color:var(--muted)}
.hero .btn{left:160px;top:230px}
.hero .ph{left:560px;top:0;width:480px;height:320px;background:radial-gradient(circle at 35% 65%,#c6d98a,#e2e6df 45%,#e8dcd2 70%,#dbe0e3)}

/* welcome */
.welcome{top:420px;left:0;width:1200px;height:480px;background:#fff}
.welcome .ph{left:140px;top:20px;width:380px;height:440px;background:linear-gradient(160deg,#e9eef2,#c9d3dc 55%,#f1b8bb)}
.welcome h2{position:absolute;left:560px;top:60px;font:700 34px "Roboto Condensed",sans-serif;color:var(--blue)}
.welcome h2 span{color:var(--red)}
.welcome .sub{left:560px;top:102px;font:400 16px "Roboto",sans-serif;color:var(--green-dark)}
.welcome p{position:absolute;left:560px;width:470px;font-size:12px;line-height:18px;color:var(--muted)}
.welcome .btn{left:560px;top:378px}

/* services */
.services{top:900px;left:0;width:1200px;height:420px;background:linear-gradient(180deg,#b5d745,#9cc42a)}
.card{position:absolute;top:90px;width:270px;text-align:center}
.card .ph{position:relative;width:270px;height:190px;border:4px solid #fff}
.card h3{margin-top:16px;font:700 19px "Roboto Condensed",sans-serif;color:#fff;text-transform:uppercase}
.card p{margin:6px auto 0;width:240px;font-size:11px;line-height:15px;color:#fff}
.card .btn{position:relative;margin-top:14px;font-size:11px;padding:8px 14px}

/* member banner */
.member{top:1320px;left:0;width:1200px;height:100px;background:var(--red)}
.member svg{left:160px;top:28px}
.member h2{position:absolute;left:226px;top:20px;font:700 38px "Roboto Condensed",sans-serif;color:#fff;line-height:1}
.member .tag{left:226px;top:58px;font:400 20px "Roboto Condensed",sans-serif;color:#ffe3e4;text-transform:uppercase;letter-spacing:.5px}
.member .join{right:160px;top:30px;background:#fff;color:var(--red);font-size:16px;padding:10px 18px}

/* blog */
.blog{top:1420px;left:0;width:1200px;height:490px;background:#fff}
.blog h2{position:absolute;top:40px;width:1200px;text-align:center;font:700 32px "Roboto Condensed",sans-serif;color:var(--dark)}
.blog svg.leaf{left:588px;top:84px}
.post{position:absolute;top:120px;width:420px;height:340px;background:var(--light)}
.post .ph{left:0;top:0;width:210px;height:340px}
.post .date{left:180px;top:30px;width:56px;height:56px;background:var(--blue);color:#fff;text-align:center;font:700 20px "Roboto Condensed",sans-serif;padding-top:8px;line-height:1}
.post .date span{display:block;font:400 11px "Roboto",sans-serif;margin-top:2px}
.post h4{position:absolute;left:250px;top:40px;width:155px;font:700 13px "Roboto",sans-serif;line-height:17px}
.post p{left:250px;top:110px;width:155px;font-size:11px;line-height:16px;color:var(--muted)}
.post .meta{left:250px;top:300px;font-size:10px;color:var(--muted);display:flex;gap:18px}

/* contact */
.contact{top:1940px;left:0;width:1200px;height:140px}
.contact .info{left:0;top:0;width:600px;height:140px;background:var(--blue);padding:22px 0 0 300px;color:#fff;font-size:12px;line-height:22px}
.contact .info div{display:flex;align-items:center;gap:8px}
.contact .ph{left:600px;top:0;width:600px;height:140px;background:linear-gradient(135deg,#eceae4,#dfe3d8 50%,#e7e4dc)}

/* footer */
.footer-nav{top:2170px;left:0;width:1200px;text-align:center}
.footer-nav a{font:400 11px "Roboto",sans-serif;color:var(--ink);text-decoration:none;margin:0 12px;text-transform:uppercase}
.footer-btns{top:2226px;left:0;width:1200px;display:flex;justify-content:center;gap:14px}
.footer-btns span{width:84px;height:22px;color:#fff;font:700 9px "Roboto",sans-serif;text-align:center;line-height:22px}
.copyright{top:2300px;left:0;width:1200px;height:68px;background:var(--dark);color:#bbb;text-align:center;font-size:11px;line-height:68px;letter-spacing:.5px}
</style>
</head>
<body>

<header class="site-header abs">
  <div class="brand abs"><span class="dot"></span><div>Verdant Fit<small>Nutritional Therapy</small></div></div>
  <a class="btn booking">Online Booking</a>
</header>

<nav class="main-nav abs">
  <a class="active">Home</a><a>Coaching/Fitness</a><a>Nutritionists</a><a>Personal Training</a><a>Nutritional Supplements</a><a>Contact Us</a>
</nav>

<section class="hero abs">
  <div class="intro abs">Introducing the</div>
  <h1>VERDANT FIT</h1>
  <p class="abs">Coaching that blends whole food nutrition, natural medicine and training to help you feel stronger every day.</p>
  <a class="btn">Read More ›</a>
  <div class="ph" role="img" aria-label="Photo of a fit woman beside a bowl of fresh vegetables and fruit"></div>
</section>

<section class="welcome abs">
  <div class="ph" role="img" aria-label="Photo of a smiling fitness couple in sportswear"></div>
  <h2><span>WELCOME TO</span> VERDANT FIT</h2>
  <div class="sub abs">Nutritional Therapy</div>
  <p style="top:150px">Our clinical nutritionists, naturopaths and trainers work together to build a plan that fits your body, your goals and your routine. Every program begins with a full health review and grows with you as you progress.</p>
  <p style="top:245px">From rehab sessions to sport coaching, we pair movement with food and natural therapies so results last. Book a visit or send a message and our team will reply within one business day.</p>
  <a class="btn">Read More ›</a>
</section>

<section class="services abs">
  <div class="card" style="left:150px">
    <div class="ph" role="img" aria-label="Photo of a group fitness class"style="background:linear-gradient(135deg,#7c8c96,#c7b7a4)"></div>
    <h3>Coaching/Fitness</h3>
    <p>Personal and small group sessions built around strength, mobility and lasting energy.</p>
    <a class="btn">Read More ›</a>
  </div>
  <div class="card" style="left:465px">
    <div class="ph" role="img" aria-label="Photo of healthy foods, fish, grains and supplements" style="background:linear-gradient(135deg,#d9c9a3,#e9a36f 50%,#b7c98a)"></div>
    <h3>Nutritional Medicine</h3>
    <p>Whole food plans and natural therapies guided by qualified clinical nutritionists.</p>
    <a class="btn">Read More ›</a>
  </div>
  <div class="card" style="left:780px">
    <div class="ph" role="img" aria-label="Photo of a rehab trainer assisting a client" style="background:linear-gradient(135deg,#5f86a8,#b9c4cc)"></div>
    <h3>Rehab Trainers</h3>
    <p>Safe recovery programs that rebuild movement after injury, surgery or long breaks.</p>
    <a class="btn">Read More ›</a>
  </div>
</section>

<section class="member abs">
  <svg class="abs" width="52" height="44" viewBox="0 0 52 44" aria-hidden="true">
    <circle cx="26" cy="11" r="9" fill="#fff"/><path d="M10 44c0-12 7-20 16-20s16 8 16 20z" fill="#fff"/>
    <circle cx="8" cy="15" r="6" fill="#fff"/><path d="M0 40c0-9 3-15 9-15 3 0 5 1 6 3-3 3-5 7-5 12z" fill="#fff"/>
    <circle cx="44" cy="15" r="6" fill="#fff"/><path d="M52 40c0-9-3-15-9-15-3 0-5 1-6 3 3 3 5 7 5 12z" fill="#fff"/>
  </svg>
  <h2>BECOME A MEMBER</h2>
  <div class="tag abs">of our fitness &amp; nutritional therapy</div>
  <a class="btn join">Join Now</a>
</section>

<section class="blog abs">
  <h2>LATEST BLOG</h2>
  <svg class="leaf abs" width="24" height="18" viewBox="0 0 24 18" aria-hidden="true"><path d="M12 18C12 8 4 6 0 6c2 7 7 10 12 12zM12 18c0-10 8-14 12-14-2 8-7 12-12 14z" fill="var(--green-dark)"/></svg>

  <article class="post" style="left:160px">
    <div class="ph" role="img" aria-label="Photo of a trainer coaching a client in the gym" style="background:linear-gradient(160deg,#8fa3b1,#d8c4b2)"></div>
    <div class="date abs">16<span>DEC</span></div>
    <h4>Simple habits that keep your training on track</h4>
    <p class="abs">Small daily changes in sleep, food and movement add up to big results over a season.</p>
    <div class="meta abs"><span>● Comments</span><span>♥ Likes</span></div>
  </article>

  <article class="post" style="left:620px">
    <div class="ph" role="img" aria-label="Photo of an athlete's muscular back in black and white" style="background:linear-gradient(160deg,#555,#aaa)"></div>
    <div class="date abs">12<span>DEC</span></div>
    <h4>Why protein timing matters after a hard session</h4>
    <p class="abs">Learn how to fuel recovery with real food and plan meals around your training week.</p>
    <div class="meta abs"><span>● Comments</span><span>♥ Likes</span></div>
  </article>
</section>

<section class="contact abs">
  <div class="info abs">
    <div><svg width="10" height="14" viewBox="0 0 10 14"><path d="M5 0a5 5 0 0 1 5 5c0 4-5 9-5 9S0 9 0 5a5 5 0 0 1 5-5z" fill="#fff"/></svg>PO Box 22, 14 Green Street, Springvale 4000</div>
    <div><svg width="10" height="10" viewBox="0 0 10 10"><circle cx="5" cy="5" r="4.5" fill="none" stroke="#fff"/><path d="M5 2v3h2" stroke="#fff" fill="none"/></svg>Mon–Fri 6:00am – 8:00pm</div>
    <div><svg width="10" height="10" viewBox="0 0 10 10"><path d="M2 0h2l1 3-2 1c1 2 2 3 4 4l1-2 3 1v2c0 1-1 1-2 1C4 10 0 6 0 2 0 1 1 0 2 0z" fill="#fff"/></svg>(00) 5550 1234</div>
    <div><svg width="12" height="9" viewBox="0 0 12 9"><rect x=".5" y=".5" width="11" height="8" fill="none" stroke="#fff"/><path d="M.5.5 6 5l5.5-4.5" stroke="#fff" fill="none"/></svg>hello@verdantfit.example</div>
  </div>
  <div class="ph" role="img" aria-label="Street map showing the studio location"></div>
</section>

<nav class="footer-nav abs">
  <a>Home</a><a>Coaching/Fitness</a><a>Nutritionists</a><a>Personal Training</a><a>Nutritional Supplements</a><a>Contact Us</a>
</nav>
<div class="footer-btns abs">
  <span style="background:var(--blue)">BOOKING</span><span style="background:var(--blue-dark)">MESSAGE</span><span style="background:var(--teal)">NEWSLETTER</span><span style="background:var(--green-dark)">CAREERS</span>
</div>

<footer class="copyright abs">COPYRIGHT © VERDANT FIT 2016. ALL RIGHTS RESERVED</footer>

</body>
</html>
```